Dunmore Acres Enterprise
Home grown grain fed beef Wholes, Halfs, Quarters
Locally raised
No Added Hormones
Call or text now to order (555) -0418-2957

```html
<!DOCTYPE html>
<html lang="en">
<head>
<meta charset="utf-8">
<title>Dunmore Acres Enterprise – Grain Fed Beef Flyer</title>
<link href="https://fonts.googleapis.com/css2?family=Alegreya:wght@500;700&family=Chonburi&display=swap" rel="stylesheet">
<style>
  :root {
    --backdrop: #4e4e4e;
    --forest: #142f33;
    --mustard: #cf8a2e;
    --cream: #f1ede1;
    --photo-light: #bdbdbd;
    --photo-dark: #3a3a3a;
  }
  * { box-sizing: border-box; margin: 0; padding: 0; }
  html, body { width: 1200px; height: 1200px; overflow: hidden; background: var(--backdrop); }
  body { position: relative; font-family: "Alegreya", Georgia, serif; }

  .flyer {
    position: absolute; left: 238px; top: 88px;
    width: 724px; height: 1024px;
    background: var(--forest); overflow: hidden;
  }
  .brand-panel {
    position: absolute; left: 0; top: 0; width: 366px; height: 360px;
    display: flex; flex-direction: column; align-items: center; justify-content: center;
    color: var(--cream); text-align: center; font-weight: 500;
  }
  .brand-name { font-size: 50px; line-height: 1; letter-spacing: 1px; }
  .brand-sub { font-size: 28px; letter-spacing: 6px; margin-top: 12px; }

  .photo { position: absolute; }
  .photo-landscape {
    left: 366px; top: 0; width: 358px; height: 360px;
    background: linear-gradient(180deg, #d6d6d6 0%, #c9c9c9 22%, #8c8c8c 28%, #9a9a9a 60%, #6f6f6f 100%);
  }
  .photo-cattle {
    left: 0; top: 428px; width: 346px; height: 330px;
    background: linear-gradient(180deg, #c8c8c8 0%, #a9a9a9 30%, #2f2f2f 45%, #3a3a3a 75%, #9d9d9d 100%);
  }

  .tagline-band {
    position: absolute; left: 0; top: 356px; width: 724px; height: 66px;
    background: var(--mustard);
    display: flex; align-items: center; justify-content: center;
    color: var(--forest); font-weight: 700; font-size: 40px;
  }

  .features { position: absolute; left: 390px; top: 456px; list-style: none; color: var(--cream); }
  .features li {
    display: flex; align-items: flex-start; gap: 10px;
    font-size: 32px; font-weight: 700; line-height: 36px; margin-bottom: 28px;
  }
  .features svg { flex: none; margin-top: -4px; }

  .contact {
    position: absolute; left: 0; top: 752px; width: 724px; height: 272px;
    background: var(--mustard); color: var(--forest);
  }
  .call-row {
    position: absolute; top: 44px; left: 62px; width: 622px;
    display: flex; align-items: center; gap: 28px;
  }
  .call-row .rule { flex: 1; height: 2px; background: var(--forest); position: relative; }
  .call-row .rule::before, .call-row .rule::after {
    content: ""; position: absolute; top: -3px; width: 6px; height: 6px;
    border: 2px solid var(--forest); border-radius: 50%;
  }
  .call-row .rule::before { left: -6px; }
  .call-row .rule::after { right: -6px; }
  .call-label { font-size: 44px; font-weight: 500; line-height: 1; }
  .phone-bar {
    position: absolute; left: 62px; top: 106px; width: 632px; height: 72px;
    background: var(--forest);
    display: flex; align-items: center; justify-content: center;
    clip-path: polygon(0 6%, 100% 0, 97% 100%, 1% 94%);
  }
  .phone-number { font-family: "Chonburi", Georgia, serif; font-size: 50px; color: var(--mustard); line-height: 1; }
  .order-note {
    position: absolute; top: 188px; left: 0; width: 100%;
    text-align: center; font-size: 31px; font-weight: 500;
  }
</style>
</head>
<body>
  <article class="flyer">
    <header class="brand-panel">
      <div class="brand-name">DUNMORE<br>ACRES</div>
      <div class="brand-sub">ENTERPRISE</div>
    </header>

    <div class="photo photo-landscape" role="img" aria-label="Black and white photo of rolling farm pasture with fence line"></div>

    <div class="tagline-band">Home grown, Grain fed beef</div>

    <div class="photo photo-cattle" role="img" aria-label="Black and white photo of black cattle standing in tall grass"></div>

    <ul class="features">
      <li>
        <svg width="40" height="38" viewBox="0 0 40 38"><path d="M2 20 L14 34 L38 4" fill="none" stroke="var(--mustard)" stroke-width="6" stroke-linecap="round" stroke-linejoin="round"/></svg>
        <span>Wholes, Halfs,<br>Quarters</span>
      </li>
      <li>
        <svg width="40" height="38" viewBox="0 0 40 38"><path d="M2 20 L14 34 L38 4" fill="none" stroke="var(--mustard)" stroke-width="6" stroke-linecap="round" stroke-linejoin="round"/></svg>
        <span>Locally raised</span>
      </li>
      <li>
        <svg width="40" height="38" viewBox="0 0 40 38"><path d="M2 20 L14 34 L38 4" fill="none" stroke="var(--mustard)" stroke-width="6" stroke-linecap="round" stroke-linejoin="round"/></svg>
        <span>No Added<br>Hormones</span>
      </li>
    </ul>

    <section class="contact">
      <div class="call-row">
        <span class="rule"></span>
        <span class="call-label">Call us</span>
        <span class="rule"></span>
      </div>
      <div class="phone-bar"><span class="phone-number">(555) -0418-2957</span></div>
      <p class="order-note">or text now to order</p>
    </section>
  </article>
</body>
</html>
```